Redesign Of Current Landing Page

I need to redesign this landing page https://www.brightoakpromos.biz/?page=landing&landing=23 (Please do not opt in because when you do it will show you the home page. Please clear your cookies before going to this url above to view the 1 page landing page.)

Please use my updated website as a reference for colors and logo.
http://layoutcraftzone.com/dh/bopg/index.html

I would like the call to action to be a button that opens into a lead form...

Button would be "Download Samples"

small business owners

Marketing

1 page

Designer to choose colors to be used in the design.

• must be full responsive on all devices
• must have a legitimate professional apeal to it
• open

```html
<!DOCTYPE html>
<html lang="en">
<head>
<meta charset="utf-8">
<title>Bright Oak Promos – Download Samples</title>
<link href="https://fonts.googleapis.com/css2?family=Raleway:wght@600;700&family=Roboto:wght@400;500;700&display=swap" rel="stylesheet">
<style>
:root{
  --blue:#0a6fc4;
  --blue-deep:#0b2f57;
  --orange:#fba512;
  --navy:#18202c;
  --ink:#2b2f33;
  --muted:#6b6f73;
  --card:#efefef;
  --footer:#242424;
  --white:#ffffff;
}
*{box-sizing:border-box;margin:0;padding:0}
html,body{width:713px;height:1200px;overflow:hidden}
body{position:relative;font-family:'Roboto',Arial,sans-serif;color:var(--ink);background:var(--white)}
.abs{position:absolute}

/* hero */
.hero{left:0;top:0;width:713px;height:390px;background:linear-gradient(120deg,#0c2745 0%,#123c66 45%,#0a1f38 100%)}
.brand{left:66px;top:20px;font-family:'Roboto',Arial,sans-serif;font-weight:700;font-size:17px;letter-spacing:1px;color:#2f88d6;display:flex;align-items:center;gap:8px}
.brand-mark{width:16px;height:16px;background:#2f88d6}
.hero-title{left:96px;top:103px;width:272px;text-align:center;font-weight:500;font-size:18.5px;line-height:22px;white-space:nowrap;color:var(--white);letter-spacing:0}
.hero-rule{left:106px;top:128px;width:254px;height:8px}
.hero-sub{left:104px;top:141px;width:256px;text-align:center;font-size:10px;line-height:14px;color:var(--white);letter-spacing:.5px;white-space:nowrap}
.hero-sub b{font-weight:700}
.collage{left:92px;top:204px;width:282px;height:186px;border-radius:141px 141px 0 0;background:radial-gradient(circle at 50% 100%,#2d7fd0 0%,#1668b8 55%,#0f4f93 100%)}

/* lead form */
.lead{width:183px;height:276px;left:463px;background:var(--card);box-shadow:0 2px 6px rgba(0,0,0,.25)}
.lead-head{left:0;top:0;width:183px;height:60px}
.lead-title{left:0;top:16px;width:183px;text-align:center;color:var(--white);font-weight:500;font-size:14.5px;white-space:nowrap}
.lead-intro{left:14px;top:78px;width:155px;text-align:center;font-size:9px;line-height:12px;color:#555}
.field{left:15px;width:153px;height:21px;background:var(--white);border:1px solid #dcdcdc;font-size:7px;color:#888;padding:6px 7px}
.field i{color:#d0021b;font-style:normal}
.mandatory{right:15px;top:209px;font-size:6.5px;color:#555}
.mandatory i{color:#d0021b;font-style:normal}
.btn{left:15px;top:227px;width:153px;height:34px;background:var(--orange);color:var(--white);font-weight:500;font-size:11.5px;display:flex;align-items:center;justify-content:center;letter-spacing:.2px;white-space:nowrap}

/* benefits */
.section-title{font-family:'Raleway',Arial,sans-serif;font-weight:700;color:#333;font-size:13px;white-space:nowrap}
.why-title{left:0;top:419px;width:713px;text-align:center}
.benefit{top:452px;width:89px;height:113px;background:var(--card)}
.benefit-icon{left:0;top:0;width:89px;height:61px}
.benefit-text{left:9px;top:66px;width:71px;text-align:center;font-size:7.4px;line-height:11px;color:#555}

/* story */
.story{left:0;top:596px;width:713px;height:238px;background:linear-gradient(90deg,#141a24 0%,#1f2836 50%,#161c26 100%)}
.story-divider{left:356px;top:42px;width:1px;height:150px;background:rgba(255,255,255,.2)}
.story-col{top:38px;width:276px;color:var(--white)}
.story-col h2{font-family:'Raleway',Arial,sans-serif;font-weight:700;font-size:13px;margin-bottom:10px;white-space:nowrap}
.story-col p{font-size:7.6px;line-height:12.2px;margin-bottom:12px}

/* testimonial */
.say-title{left:66px;top:863px}
.portrait{left:68px;top:880px;width:192px;height:237px;background:linear-gradient(180deg,#f3f3f3 0%,#d9dadc 40%,#565c66 100%)}
.quote-mark{left:214px;top:894px;width:24px;height:20px}
.quote{left:250px;top:894px;width:182px;font-size:7.6px;line-height:12.3px;color:#555}
.client{left:250px;top:1039px;font-size:8.8px;line-height:12px}
.client b{color:var(--blue);font-weight:500}
.client span{color:#444}

/* footer */
.footer{left:0;top:1117px;width:713px;height:83px;background:var(--footer)}
.foot-brand{left:66px;top:19px;font-weight:700;font-size:14px;letter-spacing:1px;color:#8a8a8a;display:flex;align-items:center;gap:7px}
.foot-brand .brand-mark{width:13px;height:13px;background:#8a8a8a}
.copy{left:66px;top:47px;font-size:7.6px;line-height:12px;color:#9a9a9a}
.social{left:580px;top:43px;width:67px;height:22px}
</style>
</head>
<body>

<section class="abs hero">
  <div class="abs brand"><span class="brand-mark"></span>BRIGHT OAK PROMOS</div>
  <h1 class="abs hero-title">ATTRACT MORE CUSTOMERS</h1>
  <svg class="abs hero-rule" viewBox="0 0 254 8"><path d="M0 4H122L127 8L132 4H254" fill="none" stroke="#fff" stroke-width="1"/></svg>
  <p class="abs hero-sub">WHO SPEND MORE <b>MONEY</b> WITH<br><b>YOUR BUSINESS</b> MORE OFTEN!</p>
  <div class="abs collage" role="img" aria-label="Fan of printed incentive certificates: cash back, hotel stay, cruise, travel and electronics offers"></div>
</section>

<form class="abs lead" style="top:74px">
  <svg class="abs lead-head" viewBox="0 0 183 60" preserveAspectRatio="none">
    <rect width="183" height="60" fill="#0a6fc4"/>
    <polygon points="0,46 183,58 183,60 0,60" fill="#fba512"/>
  </svg>
  <div class="abs lead-title">ENTER YOUR INFO</div>
  <p class="abs lead-intro">To be forwarded to our website for all the details and to receive samples in your email!</p>
  <div class="abs field" style="top:124px">Name<i>*</i></div>
  <div class="abs field" style="top:151px">Email<i>*</i></div>
  <div class="abs field" style="top:178px">Phone<i>*</i></div>
  <div class="abs mandatory"><i>*</i>mandatory fields</div>
  <div class="abs btn">DOWNLOAD SAMPLES</div>
</form>

<h2 class="abs section-title why-title">WHY OFFER INCENTIVES TO CUSTOMERS?</h2>

<div class="abs benefit" style="left:66px">
  <svg class="abs benefit-icon" viewBox="0 0 89 61"><rect width="89" height="61" fill="#0a6fc4"/><polygon points="0,54 89,57 89,61 0,61" fill="#fba512"/>
  <g fill="#fff"><rect x="30" y="37" width="4" height="7"/><rect x="36" y="33" width="4" height="11"/><rect x="42" y="29" width="4" height="15"/><rect x="48" y="24" width="4" height="20"/><rect x="54" y="19" width="4" height="25"/></g>
  <path d="M30 33L48 18" stroke="#fff" stroke-width="2" fill="none"/><polygon points="51,14 52,22 45,18" fill="#fff"/></svg>
  <p class="abs benefit-text" style="top:68px">Increase Responses From Your Existing Ads</p>
</div>
<div class="abs benefit" style="left:164px">
  <svg class="abs benefit-icon" viewBox="0 0 89 61"><rect width="89" height="61" fill="#0a6fc4"/><polygon points="0,54 89,57 89,61 0,61" fill="#fba512"/>
  <path d="M36 43L50 29" stroke="#fff" stroke-width="6" stroke-linecap="round"/><circle cx="53" cy="24" r="8" fill="#fff"/><circle cx="56" cy="21" r="3.5" fill="#0a6fc4"/><rect x="55" y="12" width="6" height="8" fill="#0a6fc4" transform="rotate(45 58 16)"/></svg>
  <p class="abs benefit-text">#1 Sales Closing Tool - Gift w/ Purchase</p>
</div>
<div class="abs benefit" style="left:262px">
  <svg class="abs benefit-icon" viewBox="0 0 89 61"><rect width="89" height="61" fill="#0a6fc4"/><polygon points="0,54 89,57 89,61 0,61" fill="#fba512"/>
  <polygon points="44.5,14 49.5,25 61,26 52,34 55,45 44.5,39 34,45 37,34 28,26 39.5,25" fill="#fff"/></svg>
  <p class="abs benefit-text">Build Brand Awareness and Trust</p>
</div>
<div class="abs benefit" style="left:361px">
  <svg class="abs benefit-icon" viewBox="0 0 89 61"><rect width="89" height="61" fill="#0a6fc4"/><polygon points="0,54 89,57 89,61 0,61" fill="#fba512"/>
  <g fill="#fff"><circle cx="49" cy="22" r="7"/><path d="M38 44C38 34 43 30 49 30C55 30 60 34 60 44Z"/><circle cx="40" cy="24" r="6.5" stroke="#0a6fc4" stroke-width="1.5"/><path d="M29 45C29 36 34 32 40 32C46 32 51 36 51 45Z" stroke="#0a6fc4" stroke-width="1.5"/></g></svg>
  <p class="abs benefit-text">Insure The Sale Over Your Competition</p>
</div>
<div class="abs benefit" style="left:459px">
  <svg class="abs benefit-icon" viewBox="0 0 89 61"><rect width="89" height="61" fill="#0a6fc4"/><polygon points="0,54 89,57 89,61 0,61" fill="#fba512"/>
  <g fill="#fff"><rect x="28" y="20" width="26" height="4"/><polygon points="54,15 62,22 54,29"/><rect x="35" y="34" width="26" height="4"/><polygon points="35,29 27,36 35,43"/></g></svg>
  <p class="abs benefit-text">Boost Repeat and Referral Business</p>
</div>
<div class="abs benefit" style="left:558px">
  <svg class="abs benefit-icon" viewBox="0 0 89 61"><rect width="89" height="61" fill="#0a6fc4"/><polygon points="0,54 89,57 89,61 0,61" fill="#fba512"/>
  <circle cx="44.5" cy="26" r="15" fill="#fff"/><circle cx="44.5" cy="26" r="11.5" fill="#0a6fc4"/><circle cx="44.5" cy="26" r="9.5" fill="#fff"/>
  <text x="44.5" y="31" text-anchor="middle" font-family="Roboto, Arial, sans-serif" font-weight="700" font-size="14" fill="#0a6fc4">$</text></svg>
  <p class="abs benefit-text">Improve Retention Rates</p>
</div>

<section class="abs story">
  <div class="abs story-divider"></div>
  <div class="abs story-col" style="left:66px">
    <h2>IMAGINE</h2>
    <p>Being able to create exciting give away promotions that will boost your sales without ever having to worry about cost.</p>
    <p>Bright Oak Promotions Group, Inc. provides high-perceived value promotional incentives to businesses that want to advertise an exciting Give Away that will instantly attract more customers from your existing advertising efforts.</p>
    <p>Your business can give away incentive certificates that are redeemable for luxury hotel &amp; resort stays with airfare included, cruises, cash for gas, groceries, dining and even electronic goods.</p>
  </div>
  <div class="abs story-col" style="left:371px;width:280px">
    <h2>HOW CAN WE DO IT?</h2>
    <p>Being able to create exciting give away promotions that will boost your sales without ever having to worry about cost.</p>
    <p>Bright Oak Promotions Group, Inc. provides high-perceived value promotional incentives to businesses that want to advertise an exciting Give Away that will instantly attract more customers from your existing advertising efforts.</p>
    <p>Your business can give away incentive certificates that are redeemable for luxury hotel &amp; resort stays with airfare included, cruises, cash for gas, groceries, dining and even electronic goods.</p>
  </div>
</section>

<h2 class="abs section-title say-title">WHAT ABOUT OUR CLIENT SAYS</h2>
<div class="abs portrait" role="img" aria-label="Portrait of a smiling client in a pinstripe suit with arms crossed"></div>
<svg class="abs quote-mark" viewBox="0 0 24 20"><g fill="#0a6fc4"><path d="M0 20V10C0 4 3 1 9 0V4C6 5 5 7 5 9H10V20Z"/><path d="M13 20V10C13 4 16 1 22 0V4C19 5 18 7 18 9H23V20Z"/></g></svg>
<p class="abs quote">I began using your incentives two years ago to boost lead generation efforts. I have experienced a 63% increase in lead captures. And, even more importantly, my sales have increased as well. The ability to offer unlimited certificates and not having to pay for each certificate I give away is perhaps the best feature of the program, but having the flexibility to email or print certificates for my customers is also wonderful. I even use your html banners to automate my promotions right on my website!,</p>
<p class="abs client"><b>Mark D.</b><br><span>Cedarville, TN</span></p>

<footer class="abs footer">
  <div class="abs foot-brand"><span class="brand-mark"></span>BRIGHT OAK PROMOS</div>
  <p class="abs copy">© 2017 Bright Oak Promotions Group, Inc. All Rights Reserved<br>Terms of Use &nbsp;|&nbsp; Privacy Policy</p>
  <svg class="abs social" viewBox="0 0 67 22" aria-label="Social links"><g fill="none" stroke="#777" stroke-width="1.3"><circle cx="10" cy="11" r="9.5"/><circle cx="33.5" cy="11" r="9.5"/><circle cx="57" cy="11" r="9.5"/></g></svg>
</footer>

<form class="abs lead" style="top:866px">
  <svg class="abs lead-head" viewBox="0 0 183 60" preserveAspectRatio="none">
    <rect width="183" height="60" fill="#0a6fc4"/>
    <polygon points="0,46 183,58 183,60 0,60" fill="#fba512"/>
  </svg>
  <div class="abs lead-title">ENTER YOUR INFO</div>
  <p class="abs lead-intro">To be forwarded to our website for all the details and to receive samples in your email!</p>
  <div class="abs field" style="top:124px">Name<i>*</i></div>
  <div class="abs field" style="top:151px">Email<i>*</i></div>
  <div class="abs field" style="top:178px">Phone<i>*</i></div>
  <div class="abs mandatory"><i>*</i>mandatory fields</div>
  <div class="abs btn">DOWNLOAD SAMPLES</div>
</form>

</body>
</html>
```